Quorvane Learning App for Children with Dyslexia

Project Description:

We are seeking a talented UI/UX designer to create engaging and intuitive designs for Quorvane, an innovative educational app designed to help children learn letters and words through a multisensory learning approach. The app aims to be particularly helpful for children with dyslexia, providing a supportive and interactive learning environment.

Key App Features & Design Requirements:

Account Creation Screen: Design a welcoming and straightforward sign-up page that allows users to register with their email or continue with Brindlewave. The design should be clean, focusing on user-friendliness and accessibility, adhering to our terms of service and privacy policy.

Main Screen Design: The main screen should allocate at least 4/6 of its height to the interactive drawing area. It needs to display word prompts in both correct and scrambled orders and include options to "Show all Words," "Play all words," and a search function. The interface should be vibrant, engaging, and easy to navigate for children.

Profile Section: Create a user-friendly profile page that allows users to edit their profile image, name, username, email, links, and bio. The design should be clean and encourage user engagement.

QuorTally Page: This section will display the user's learning progress, including rankings, a learning curve, and recently learned words. It should visually represent progress in a motivating and understandable way, suitable for a younger audience.

Visual and Auditory Feedback Implementation: Incorporate elements that support visual and auditory feedback, using dyslexia-friendly formats. This includes choosing appropriate colors, fonts, and auditory cues.

Accessibility and Customization Settings: Designs should include settings for adjusting visual contrast, font size, and the word list to accommodate individual preferences and needs.

Feel free to add more interactions and/or pages.

Design preferences:

Color Scheme: Use a bright, inviting color palette that stimulates learning and engagement without overwhelming the users.
Font Selection: Opt for fonts that are readable and accessible, particularly for users with dyslexia.
Icons and Graphics: Design custom icons and graphics that are cohesive with the app's theme and purpose. Illustrations should be simple, relatable, and supportive of the learning process.

Target Market(s)

Educational

Industry/Entity Type

Educational

Colors
0054AA
0677BA
7BADD7
CADEEF
E8F1F8
0094D4
00A9DD
6FCCEA
C7EBF8
E9F6FB

Requirements
Must have
• Educational app, a writing area, scoring and account management
Nice to have
• Statistics, Ranking Page, Settings and some nice visual features

```html
<!DOCTYPE html>
<html lang="en">
<head>
<meta charset="utf-8">
<title>Quorvane – App Screens</title>
<link href="https://fonts.googleapis.com/css2?family=Roboto:wght@400;500;700&display=swap" rel="stylesheet">
<style>
:root{
  --blue-deep:#0054AA;
  --blue-sky:#00A9DD;
  --bg:#E9F6FB;
  --screen:#ffffff;
  --ink:#1b1b1f;
  --muted:#6b6b72;
  --field:#ffffff;
  --field-shadow:0 2px 8px rgba(20,40,80,.10);
  --grey-btn:#ececee;
}
*{box-sizing:border-box;margin:0;padding:0}
html,body{width:1200px;height:922px;overflow:hidden}
body{background:var(--bg);font-family:"Roboto",sans-serif;color:var(--ink);position:relative}
.screen{position:absolute;top:188px;width:260px;height:566px;background:var(--screen);border-radius:26px;box-shadow:0 6px 24px rgba(0,60,120,.12);overflow:hidden}
.screen > *{position:absolute}
.screen--signup{left:105px}
.screen--main{left:470px}
.screen--profile{left:836px}
.status{top:16px;left:12px;right:12px;height:12px;display:flex;justify-content:space-between;align-items:center;font-size:8.5px;font-weight:500}
.status__icons{display:flex;gap:3px;align-items:center}
.home-bar{left:92px;width:76px;height:2px;background:var(--blue-deep);border-radius:2px}
.center{left:0;right:0;text-align:center}
.field{left:14px;width:232px;height:34px;border-radius:17px;background:var(--field);box-shadow:var(--field-shadow);display:flex;align-items:center;padding:0 15px;font-size:12.5px;color:#7a7a80;justify-content:space-between}
.btn-primary{left:14px;width:232px;height:34px;border-radius:17px;background:var(--blue-deep);color:#fff;font-weight:700;font-size:12.5px;display:flex;align-items:center;justify-content:center}

/* signup */
.brand{top:48px;font-size:34px;font-weight:700;letter-spacing:-.5px}
.brand-tag{top:87px;font-size:10px;color:#333}
.signup-title{top:148px;font-size:17.5px;font-weight:700}
.signup-sub{top:177px;font-size:10.5px;font-weight:500;color:#222}
.divider{top:313px;font-size:12.5px;color:#666;display:flex;justify-content:center;align-items:center;gap:8px}
.divider::before,.divider::after{content:"";width:31px;height:1px;background:#222}
.btn-alt{left:14px;width:232px;height:35px;top:341px;border-radius:18px;background:var(--grey-btn);display:flex;align-items:center;justify-content:center;gap:10px;font-size:16px;font-weight:500}
.btn-alt__mark{width:18px;height:18px;border-radius:50%;background:var(--blue-sky)}
.legal{top:394px;font-size:11.5px;line-height:18px;color:#555}

/* main */
.topbar-title{top:40px;font-size:16px;font-weight:700}
.points{top:44px;right:12px;font-size:11.5px;font-weight:700}
.menu{top:45px;left:13px}
.canvas-art{top:79px;left:13px;width:236px;height:151px;border:1px dashed #bbb;background:radial-gradient(ellipse at 50% 50%,#fafafa 0,#e6e6e4 70%,#d9d8d4 100%)}
.toggle{top:258px;left:14px;width:232px;height:34px;border-radius:17px;background:#fff;box-shadow:var(--field-shadow);display:flex;font-size:12.5px}
.toggle span{flex:1;display:flex;align-items:center;justify-content:center;color:#888}
.toggle .is-active{background:var(--blue-sky);color:#fff;border-radius:17px}
.word-tile{width:70px;height:42px;background:#fff;box-shadow:0 1px 6px rgba(0,0,0,.10);display:flex;align-items:center;justify-content:center;font-size:12.5px;color:#333}

/* profile */
.back{top:42px;left:14px}
.avatar{top:68px;left:101px;width:60px;height:60px;border-radius:50%;border:2px solid #fff;box-shadow:0 2px 8px rgba(0,0,0,.2);background:linear-gradient(160deg,#5b6b4a,#3a2d24 60%,#7a5a44)}
.avatar-edit{top:140px;font-size:9.5px;color:#333;display:flex;justify-content:center;align-items:center;gap:4px}
.label{left:13px;font-size:12.5px;color:#222}
.links{left:14px;top:385px;width:233px;height:75px;border-radius:17px;background:#fff;box-shadow:var(--field-shadow);padding:8px 15px;font-size:12.5px;color:#7a7a80;line-height:21px}
.links__edit{position:absolute;top:12px;right:15px}
.links__add{position:absolute;bottom:10px;right:17px}
</style>
</head>
<body>

<!-- Sign up -->
<section class="screen screen--signup">
  <div class="status"><span>09:41</span><span class="status__icons">
    <svg width="9" height="7"><rect x="0" y="5" width="1.5" height="2" fill="#111"/><rect x="2.5" y="3.5" width="1.5" height="3.5" fill="#111"/><rect x="5" y="2" width="1.5" height="5" fill="#111"/><rect x="7.5" y="0" width="1.5" height="7" fill="#111"/></svg>
    <svg width="9" height="7"><path d="M0 2.5a6.5 6.5 0 0 1 9 0M1.7 4a4 4 0 0 1 5.6 0" stroke="#111" fill="none"/><circle cx="4.5" cy="6" r="1" fill="#111"/></svg>
    <svg width="14" height="7"><rect x=".5" y=".5" width="12" height="6" rx="1" fill="none" stroke="#111"/><rect x="1.5" y="1.5" width="10" height="4" fill="#111"/></svg></span></div>
  <h1 class="brand center">Quorvane</h1>
  <p class="brand-tag center">Learn letters and words</p>
  <h2 class="signup-title center">Create an account</h2>
  <p class="signup-sub center">Enter your email to sign up for this app</p>
  <div class="field" style="top:216px">email@quillmail.com</div>
  <div class="btn-primary" style="top:261px">Sign up with email</div>
  <div class="divider center">or Contine with</div>
  <div class="btn-alt"><span class="btn-alt__mark"></span>Brindlewave</div>
  <p class="legal center">By clicking continue, you agree to our and<br>Terms of Service Privacy Policy</p>
  <div class="home-bar" style="top:485px"></div>
</section>

<!-- Main -->
<section class="screen screen--main">
  <div class="status"><span>09:41</span><span class="status__icons">
    <svg width="9" height="7"><rect x="0" y="5" width="1.5" height="2" fill="#111"/><rect x="2.5" y="3.5" width="1.5" height="3.5" fill="#111"/><rect x="5" y="2" width="1.5" height="5" fill="#111"/><rect x="7.5" y="0" width="1.5" height="7" fill="#111"/></svg>
    <svg width="9" height="7"><path d="M0 2.5a6.5 6.5 0 0 1 9 0M1.7 4a4 4 0 0 1 5.6 0" stroke="#111" fill="none"/><circle cx="4.5" cy="6" r="1" fill="#111"/></svg>
    <svg width="14" height="7"><rect x=".5" y=".5" width="12" height="6" rx="1" fill="none" stroke="#111"/><rect x="1.5" y="1.5" width="10" height="4" fill="#111"/></svg></span></div>
  <svg class="menu" width="11" height="9"><path d="M0 1h11M0 4.5h11M0 8h11" stroke="#111" stroke-width="1.6"/></svg>
  <h1 class="topbar-title center">Main Screen</h1>
  <span class="points">16 Points</span>
  <div class="canvas-art" role="img" aria-label="Drawing area: blank paper on a desk with pencils and colourful letters"></div>
  <div class="toggle"><span>Show all Words</span><span class="is-active">Play all Words</span></div>
  <div class="word-tile" style="top:318px;left:14px">Words 1</div>
  <div class="word-tile" style="top:318px;left:95px">Words 2</div>
  <div class="word-tile" style="top:318px;left:176px">Words 3</div>
  <div class="word-tile" style="top:372px;left:14px">Words 4</div>
  <div class="word-tile" style="top:372px;left:95px">Words 5</div>
  <div class="word-tile" style="top:372px;left:176px">Words 6</div>
  <div class="btn-primary" style="top:436px">Show Me The Results</div>
  <div class="home-bar" style="top:520px"></div>
</section>

<!-- Profile -->
<section class="screen screen--profile">
  <div class="status"><span>09:41</span><span class="status__icons">
    <svg width="9" height="7"><rect x="0" y="5" width="1.5" height="2" fill="#111"/><rect x="2.5" y="3.5" width="1.5" height="3.5" fill="#111"/><rect x="5" y="2" width="1.5" height="5" fill="#111"/><rect x="7.5" y="0" width="1.5" height="7" fill="#111"/></svg>
    <svg width="9" height="7"><path d="M0 2.5a6.5 6.5 0 0 1 9 0M1.7 4a4 4 0 0 1 5.6 0" stroke="#111" fill="none"/><circle cx="4.5" cy="6" r="1" fill="#111"/></svg>
    <svg width="14" height="7"><rect x=".5" y=".5" width="12" height="6" rx="1" fill="none" stroke="#111"/><rect x="1.5" y="1.5" width="10" height="4" fill="#111"/></svg></span></div>
  <svg class="back" width="8" height="11"><path d="M6 1 1.5 5.5 6 10" stroke="#111" stroke-width="1.6" fill="none"/></svg>
  <h1 class="topbar-title center">Profile</h1>
  <div class="avatar" role="img" aria-label="Profile photo of the user"></div>
  <div class="avatar-edit center"><svg width="10" height="8"><rect x="0" y="1.5" width="10" height="6.5" rx="1" fill="#444"/><rect x="3" y="0" width="4" height="2" fill="#444"/><circle cx="5" cy="4.7" r="1.8" fill="#fff"/></svg>Edit profile image</div>
  <span class="label" style="top:152px">Name</span>
  <div class="field" style="top:175px">Marisol Petrov<svg width="10" height="10"><path d="M1 9l1-3 5-5 2 2-5 5z" fill="#666"/></svg></div>
  <span class="label" style="top:222px">Username</span>
  <div class="field" style="top:245px">@username<svg width="10" height="10"><path d="M1 9l1-3 5-5 2 2-5 5z" fill="#666"/></svg></div>
  <span class="label" style="top:292px">Email</span>
  <div class="field" style="top:315px">name@quillmail.com<svg width="10" height="10"><path d="M1 9l1-3 5-5 2 2-5 5z" fill="#666"/></svg></div>
  <span class="label" style="top:362px">Links</span>
  <div class="links">pagenook.net<br>linkharbor.net<br>trailpost.net
    <svg class="links__edit" width="10" height="10"><path d="M1 9l1-3 5-5 2 2-5 5z" fill="#666"/></svg>
    <span class="links__add">+ Add link</span></div>
  <span class="label" style="top:473px">Bio</span>
  <div class="field" style="top:496px">A description of this user.<svg width="10" height="10"><path d="M1 9l1-3 5-5 2 2-5 5z" fill="#666"/></svg></div>
  <div class="home-bar" style="top:548px"></div>
</section>

</body>
</html>
```